Verdant Turfworks by MO

Design a eye catching EDDM postcard for Lawn Care business... 6.5" x 8" EDDM Postcards with required bleed points

There are a few EDDM rules to follow which are.

1. Be sure to add your Postal Indicia it needs to read
“PRST STD ECRWSS U.S. POSTAGE PAID EDDM RETAIL”
in the top right area of your EDDM Flyer Postcard

2. The address area also needs to be filled in with
“****ECRWSS**** Local Postal Customer”

3. Both of these items need to be present on the same side for example both on the back of your EDDM mailer.
Please see the image on the side here for a visual description on how to set up your EDDM mailer correctly. (Attached Sample Template)

Target Market(s)

Home Owners that has a Lawn Care need

Industry/Entity Type

Lawn Care

Font styles to use
Serif

Colors

Designer to choose colors to be used in the design.

Requirements
Must have
• A beautiful background that capture the homeowner eyes when they open their mailbox and see this small card.
• My number: 713-554-0287
• My Name & Email: Malcolm Ostrander - maostgreens@quellmail.com

```html
<!DOCTYPE html>
<html lang="en">
<head>
<meta charset="utf-8">
<title>Verdant Turfworks by MO – Lawn Service Postcard</title>
<link rel="stylesheet" href="https://fonts.googleapis.com/css2?family=Archivo:wght@700;800;900&family=Oswald:wght@500;600;700&family=Open+Sans:ital,wght@1,600&display=swap">
<style>
  :root {
    --white: #ffffff;
    --ink: #1a1a1a;
    --red: #e8141b;
    --blue: #1534d6;
    --green-light: #8fd64a;
    --green-mid: #6bbf1e;
    --green-deep: #3f8f0c;
    --yellow: #f4ee1a;
    --burst-inner: #fff36a;
    --burst-outer: #ffcc12;
  }
  * { margin: 0; padding: 0; box-sizing: border-box; }
  html, body { width: 1200px; height: 975px; overflow: hidden; background: var(--white); }
  .postcard { position: relative; width: 1200px; height: 975px; overflow: hidden; background: var(--white); }

  .header { position: absolute; left: 0; top: 0; width: 1200px; height: 200px; background: var(--white); }
  .brand {
    position: absolute; left: 40px; top: 70px; width: 410px;
    font-family: "Archivo", sans-serif; font-weight: 800; font-size: 40px; line-height: 1.05;
    color: var(--ink); display: flex; align-items: center; gap: 14px;
  }
  .brand-dot { width: 26px; height: 26px; border-radius: 50%; background: var(--green-mid); flex: none; }
  .contact { position: absolute; left: 460px; top: 22px; width: 720px; text-align: center; }
  .cta {
    font-family: "Oswald", sans-serif; font-weight: 600; color: var(--red);
    font-size: 34px; line-height: 1; white-space: nowrap; letter-spacing: -0.3px;
  }
  .cta .big { font-size: 49px; font-weight: 700; }
  .phone {
    font-family: "Archivo", sans-serif; font-weight: 900; color: var(--blue);
    font-size: 57px; line-height: 1; margin-top: 4px;
  }
  .owner, .email {
    font-family: "Archivo", sans-serif; font-weight: 800; color: var(--blue); line-height: 1.35;
  }
  .owner { font-size: 23px; margin-top: 4px; }
  .email { font-size: 24px; }

  .tagline-band {
    position: absolute; left: 0; top: 200px; width: 1200px; height: 72px;
    background: linear-gradient(90deg, var(--green-light), var(--green-mid) 60%, var(--green-deep));
    display: flex; align-items: center; justify-content: center;
  }
  .tagline {
    font-family: "Open Sans", sans-serif; font-style: italic; font-weight: 600;
    color: var(--white); font-size: 33px; margin-left: 30px;
  }
  .seam { position: absolute; left: 0; top: 272px; width: 1200px; height: 16px; background: #b4ee78; }

  .hero-photo {
    position: absolute; left: 0; top: 288px; width: 1200px; height: 396px;
    background: linear-gradient(90deg, #2c3a1c 0%, #c21a2c 18%, #e63a4c 45%, #4f9a1e 70%, #6fc02a 100%);
  }
  .inset-photo {
    position: absolute; left: 840px; top: 298px; width: 340px; height: 268px;
    border: 5px solid var(--white);
    background: linear-gradient(180deg, #b9b0a0 0%, #8c8676 45%, #5f8a2e 75%, #4a3a2a 100%);
  }
  .headline {
    position: absolute; left: 36px; top: 497px;
    font-family: "Archivo", sans-serif; font-weight: 900; color: var(--white);
    font-size: 65px; letter-spacing: -1px; line-height: 1;
    text-shadow: 0 3px 8px rgba(0,0,0,0.55);
  }

  .services-panel {
    position: absolute; left: 0; top: 684px; width: 1200px; height: 291px;
    background: linear-gradient(90deg, var(--green-light), var(--green-mid) 55%, var(--green-deep));
    border-top: 4px solid #a8e86a;
  }
  .services-title {
    position: absolute; left: 42px; top: 730px;
    font-family: "Archivo", sans-serif; font-weight: 900; color: var(--yellow);
    font-size: 53px; letter-spacing: 1px; line-height: 1; text-shadow: 0 2px 5px rgba(0,0,0,0.45);
  }
  .service {
    position: absolute; font-family: "Archivo", sans-serif; font-weight: 800;
    color: var(--white); font-size: 38px; letter-spacing: 0.5px; line-height: 1; white-space: nowrap;
    text-shadow: 0 2px 4px rgba(0,0,0,0.45);
  }

  .promo-burst { position: absolute; left: 936px; top: 558px; width: 232px; height: 232px; }
  .promo-text {
    position: absolute; left: 936px; top: 558px; width: 232px; height: 232px;
    display: flex; flex-direction: column; align-items: center; justify-content: center;
    transform: rotate(8deg); font-family: "Oswald", sans-serif; color: var(--red); text-align: center;
  }
  .promo-text .line { font-size: 31px; font-weight: 700; line-height: 1.05; }
  .promo-text .sub { font-size: 17px; font-weight: 600; margin-top: 4px; }
</style>
</head>
<body>
<main class="postcard">
  <header class="header">
    <div class="brand"><span class="brand-dot"></span><span>Verdant Turfworks by MO</span></div>
    <div class="contact">
      <p class="cta">CALL US <span class="big">TODAY</span> FOR YOUR <span class="big">FREE ESTIMATE!</span></p>
      <p class="phone">713-554-0287</p>
      <p class="owner">Malcolm Ostrander</p>
      <p class="email">maostgreens@quellmail.com</p>
    </div>
  </header>

  <section class="tagline-band"><p class="tagline">We take care of your lawn and landscaping needs!</p></section>
  <div class="seam"></div>

  <div class="hero-photo" role="img" aria-label="Close-up of a red lawn mower cutting bright green grass"></div>
  <div class="inset-photo" role="img" aria-label="House entrance with neatly landscaped shrubs, mulch beds and lawn"></div>
  <h1 class="headline">NEED LAWN SERVICE?</h1>

  <section class="services-panel" aria-label="Services"></section>
  <h2 class="services-title">Services Included</h2>
  <p class="service" style="left:38px; top:804px;">Weekly Lawn Maintenance</p>
  <p class="service" style="left:38px; top:858px;">Tree, Concrete &amp; Debris Removal</p>
  <p class="service" style="left:40px; top:910px;">Irrigation System</p>
  <p class="service" style="left:716px; top:806px;">Landscape Installation</p>
  <p class="service" style="left:716px; top:858px;">Land Clearing</p>
  <p class="service" style="left:716px; top:912px;">Skid Steer Services</p>

  <svg class="promo-burst" viewBox="0 0 200 200" aria-hidden="true">
    <defs>
      <radialGradient id="burstFill" cx="50%" cy="50%" r="55%">
        <stop offset="0%" stop-color="#fff36a"/>
        <stop offset="100%" stop-color="#ffcc12"/>
      </radialGradient>
    </defs>
    <polygon fill="url(#burstFill)" points="200,100 178.5,115.6 192.4,138.3 166.5,144.5 170.7,170.7 144.5,166.5 138.3,192.4 115.6,178.5 100,200 84.4,178.5 61.7,192.4 55.5,166.5 29.3,170.7 33.5,144.5 7.6,138.3 21.5,115.6 0,100 21.5,84.4 7.6,61.7 33.5,55.5 29.3,29.3 55.5,33.5 61.7,7.6 84.4,21.5 100,0 115.6,21.5 138.3,7.6 144.5,33.5 170.7,29.3 166.5,55.5 192.4,61.7 178.5,84.4"/>
  </svg>
  <div class="promo-text">
    <span class="line">FREE MOWING</span>
    <span class="line">SPECIAL</span>
    <span class="sub">For New Customers</span>
  </div>
</main>
</body>
</html>
```